New Design for our Velorin Gran Reserva Brandy, it is the label design for the bottle label

We need a new bottle label for our Brandy Gran Reserva that we want to bring to the market.

Please have a look at all our current bottles and labels and the feel of our company under www.velorin-example.ch

The bottle that we will be using for the brand is a different one than the one that we already have, the design of the bottle is attached with a document.

I have also attached a briefing in regards to Brandy in general for your information.

### 1. What is Brandy?
Brandy is a distilled spirit made from fermented wine or other fruit wines. It is traditionally aged in oak barrels, which gives it its characteristic color and rich flavor. The aging process in oak is essential for developing the aromas and quality of the brandy.

### 2. What is Brandy Reserva?
A Brandy labeled as "Reserva" has undergone a longer aging process, typically at least 2 to 3 years, in oak barrels. This aging gives the brandy a deeper, more complex flavor profile and a darker color. "Reserva" is often an indication of higher quality.

### 3. Who enjoys drinking Brandy?
Brandy is typically favored by those who appreciate a deep, rich tasting experience. This often includes older consumers who value the time-aged complexity of the spirit. However, Brandy is also gaining popularity among younger people, especially through cocktails and modern serving styles.

### 4. Why is Brandy trending?
Brandy is experiencing a resurgence as consumers increasingly value quality and artisanal production methods. Its versatility in cocktails and association with traditional, luxurious experiences have also contributed to its renewed popularity.

### 5. What colors would be associated with Brandy?
The typical colors associated with Brandy are warm gold, amber, and deep golden-brown tones. These colors reflect the aging process in oak barrels and the richness of the flavors. Other associated colors might include dark brown and mahogany.

### 6. What is important to customers when buying Brandy?
Customers care about the origin of the Brandy, the aging time, the quality of the ingredients, the production method, and the brand. They also pay attention to the prestige of the product and the authenticity of the production.

### 7. What is not important to customers when buying Brandy?
For many customers, the price and packaging (unless it’s especially exclusive) may be less important than the quality and taste of the Brandy. The distillery name might be less significant if it isn’t tied to a particular reputation.

### 8. What do customers know about Swiss Brandy?
Swiss Brandy is still relatively unknown in many markets, but customers who are familiar with it appreciate the precision and quality of Swiss production. Swiss Brandy is assumed to be made with care and under strict quality standards.

### 9. What is Brandy Gran Reserva?
**Brandy Gran Reserva** is an even higher quality and longer-aged version of Brandy. Generally, a Gran Reserva is aged for at least 5 to 10 years or more in oak barrels. This extended aging process gives the Brandy an especially deep, complex flavor profile and often a darker, richer color. Gran Reserva is often regarded as the top-tier product within a Brandy range and appeals to discerning consumers who value quality, refinement, and a luxurious tasting experience.

The label “Gran Reserva” thus indicates the highest quality level for Brandies, similar to other spirits (like wine or whisky), where the aging time is a critical factor.

### 10. What emotions are associated with Brandy?
Brandy is often associated with luxury, relaxation, and comfort. It evokes feelings of tradition, elegance, and sophistication. Drinking Brandy is frequently seen as a moment of reflection and enjoyment.

### 11. How should Brandy be marketed?
Brandy should be marketed with a focus on its artisanal production, quality, and tradition. A narrative around the product, its aging, and origin can help create an emotional connection with the customer. The marketing should also emphasize the versatility of Brandy, whether consumed neat or in cocktails.

### 12. Sales test and label design for Velorin Brandy
For a sales test, I would suggest a tasting in an upscale setting, perhaps paired with a storytelling presentation highlighting the history of the 6-year aged Brandy and its aging in oak barrels.

**Label design**:
The label should reflect the exclusivity of the product, with an elegant, minimalist design. Colors like deep gold, mahogany, and a hint of deep blue could be used to emphasize the aging and quality of the Brandy. The label should include information about the aging time, the use of oak barrels, and a brief story about the Brandy’s production. A seal or embossing highlighting the craftsmanship would also be fitting.

Target Market(s)

Customers that like Brandy

Requirements
Must have
• the Alcohol % must be included on the label as well as our address.

```html
<!DOCTYPE html>
<html lang="en">
<head>
<meta charset="utf-8">
<title>Velorin Gran Reserva Brandy – Label</title>
<link rel="stylesheet" href="https://fonts.googleapis.com/css2?family=Cinzel:wght@400;700&family=Grenze+Gotisch:wght@600&display=swap">
<style>
  :root {
    --page: #ffffff;
    --amber-light: #f2a52a;
    --amber: #e8901a;
    --amber-deep: #c86f0c;
    --print: #ffffff;
    --ink: #141414;
  }
  * { margin: 0; padding: 0; box-sizing: border-box; }
  html, body { width: 1200px; height: 960px; overflow: hidden; background: var(--page); }
  .canvas { position: relative; width: 1200px; height: 960px; }

  .label {
    position: absolute; left: 476px; top: 318px; width: 248px; height: 480px;
    background: linear-gradient(90deg, var(--amber-deep) 0%, var(--amber) 18%, var(--amber-light) 50%, var(--amber) 82%, var(--amber-deep) 100%);
    color: var(--print);
    text-align: center;
  }
  .brand-name {
    position: absolute; left: 0; right: 0; top: 68px;
    font-family: "Cinzel", serif; font-weight: 700; font-size: 24px; letter-spacing: 1px; line-height: 1;
  }
  .brand-sub {
    position: absolute; left: 0; right: 0; top: 96px;
    font-family: "Cinzel", serif; font-weight: 700; font-size: 10px; line-height: 1.25; letter-spacing: 0.5px;
  }
  .rule { position: absolute; left: 42px; right: 42px; height: 1px; background: var(--print); opacity: 0.8; }
  .rule.top { top: 148px; }
  .rule.bottom { top: 210px; }
  .product {
    position: absolute; left: 0; right: 0; top: 148px;
    font-family: "Grenze Gotisch", serif; font-weight: 600; font-size: 50px; line-height: 1;
  }
  .grade {
    position: absolute; left: 0; right: 0; top: 191px;
    font-family: "Cinzel", serif; font-size: 11px; letter-spacing: 3px;
  }
  .established {
    position: absolute; left: 0; right: 0; top: 226px;
    font-family: "Cinzel", serif; font-size: 11px; letter-spacing: 3px;
  }
  .emblem {
    position: absolute; left: 74px; top: 256px; width: 108px; height: 100px;
    background: linear-gradient(180deg, rgba(255,255,255,0.35), rgba(255,255,255,0.2));
  }
  .strength {
    position: absolute; left: 0; right: 0; top: 370px;
    font-family: "Cinzel", serif; font-size: 11px; letter-spacing: 3px;
  }

  .house-mark {
    position: absolute; left: 82px; top: 802px; width: 110px; text-align: center; color: var(--ink);
  }
  .house-mark .name { font-family: "Cinzel", serif; font-weight: 700; font-size: 22px; line-height: 1; }
  .house-mark .sub { font-family: "Cinzel", serif; font-weight: 700; font-size: 9px; line-height: 1.2; margin-top: 3px; }
</style>
</head>
<body>
<div class="canvas">
  <section class="label" aria-label="Velorin Gran Reserva Brandy bottle label">
    <div class="brand-name">Velorin</div>
    <div class="brand-sub">SWISS<br>DISTILLERY</div>
    <div class="rule top"></div>
    <div class="product">brandy</div>
    <div class="grade">Gran Reserva</div>
    <div class="rule bottom"></div>
    <div class="established">EST. 2024</div>
    <div class="emblem" role="img" aria-label="Line emblem of a distillery house framed by three ears of grain"></div>
    <div class="strength">ALCOHOL 55%</div>
  </section>

  <div class="house-mark">
    <div class="name">Velorin</div>
    <div class="sub">SWISS<br>DISTILLERY</div>
  </div>
</div>
</body>
</html>
```